Business Card & Logo Design - Hedge Fund

We need a business card and logo design for a hedge fund. The hedge fund is named Morvane Holdings LLC. Morvane Holdings was created by finance professors and the strategy is based academic research that looks for patterns in stock prices. The design should look conservative, solid, strong. We favor a classic style - nothing flashy. The logo can relate to the name Morvane Holdings, or it could involve a symbol design that connotes "science" . We are open to ideas. We do not want alot of colors - but if any, color - blue is preferred. The font that seems to look best for the name (Morvane Holdings) is arial black. We are open to ideas. Most important - we want to see a mock up of an actual business card with the logo concept embedded. The business card should include space for : company name, individual name, position title, cell phone, address. We hope to have this work done by Sept. 8.

Target Market(s)

We will be meeting with and giving the business card to institutions and high net worth individuals.

Industry/Entity Type

Investment Advisory

Contact Information for Business Card

Company name - Morvane Holdings LLC
Individual name - Peter Vosk
Title - Portfolio Manager
Cell - (482) 555-0137
Address - 2750 Birchwell Lane, Suite 300, Atlanta GA 30327

Font styles to use
Other font styles liked:
• Arial

Colors
3277b5
0255a3
85acd3
cedeed
fdf9cf
d9d9d9
e6e6e6
f04a50
6b449b

Requirements
Must have
• Must have card details that are sited above.
• We would like a logo related to the name (Morvane Holdings) or concept of the fund.
Nice to have
• We want conservative / understated / clean crisp look.
• If any colors - we prefer conservative appearance - blue / gray.
• I have enclosed an example of a card style that looks attractive - please do not exactly copy this card. This is not our company or logo. I feel the layout is attractive - just as an example
Should not have
• Avoid too much color.
• I have selected some preferred colors. Please do not use all of the colors - I have selected a few that might work - but I am not sure. We are open to your ideas so please do not feel the need to use all or any of these.

```html
<!DOCTYPE html>
<html lang="en">
<head>
<meta charset="utf-8">
<title>Morvane Holdings LLC – Business Card</title>
<link rel="stylesheet" href="https://fonts.googleapis.com/css2?family=Arimo:wght@400;700&display=swap">
<style>
  :root {
    --backdrop: #8a8a8a;
    --card-light: #f3f3f3;
    --card-navy: #25226e;
    --navy: #1f1a78;
    --gray: #8f8f8f;
    --ink: #262626;
    --rule: #9a9a9a;
    --white: #ffffff;
  }
  * { margin: 0; padding: 0; box-sizing: border-box; }
  html, body { width: 1200px; height: 900px; overflow: hidden; }
  body {
    background: var(--backdrop);
    font-family: "Arimo", Arial, sans-serif;
    position: relative;
  }
  .card {
    position: absolute;
    top: 200px;
    width: 310px;
    height: 502px;
  }
  .card--front {
    left: 253px;
    background: var(--card-light);
    border-radius: 58px 0 58px 0;
  }
  .card--back {
    left: 627px;
    background: linear-gradient(160deg, #272475 0%, var(--card-navy) 60%, #221f66 100%);
    border-radius: 0 58px 0 58px;
  }
  .brand {
    position: absolute;
    left: 0; right: 0;
    display: flex;
    flex-direction: column;
    align-items: center;
  }
  .brand__mark {
    width: 64px; height: 64px;
    margin-bottom: 22px;
  }
  .brand__name {
    font-weight: 700;
    font-size: 19px;
    letter-spacing: 1px;
    text-transform: uppercase;
    white-space: nowrap;
  }
  .brand__rule {
    width: 214px;
    height: 1px;
    margin-top: 6px;
  }
  .card--front .brand { top: 80px; }
  .card--front .brand__mark { background: var(--navy); }
  .card--front .brand__name { color: var(--navy); }
  .card--front .brand__rule { background: var(--rule); }
  .card--back .brand { top: 176px; }
  .card--back .brand__mark { background: var(--white); }
  .card--back .brand__name { color: var(--white); }
  .card--back .brand__rule { background: var(--white); }

  .contact {
    position: absolute;
    left: 35px;
    top: 329px;
    font-size: 14px;
    line-height: 18px;
    color: var(--ink);
  }
  .contact__name {
    font-size: 17px;
    font-weight: 700;
    text-transform: uppercase;
    line-height: 20px;
  }
  .contact__first { color: var(--navy); }
  .contact__last { color: var(--gray); }
  .contact__phone {
    display: flex;
    align-items: center;
    gap: 5px;
    margin-top: 12px;
  }
  .contact__phone svg { width: 9px; height: 13px; }
  .contact__company {
    margin-top: 11px;
    color: var(--navy);
    text-transform: uppercase;
  }
</style>
</head>
<body>
  <section class="card card--front">
    <div class="brand">
      <div class="brand__mark"></div>
      <div class="brand__name">Morvane Holdings</div>
      <div class="brand__rule"></div>
    </div>
    <div class="contact">
      <p class="contact__name"><span class="contact__first">Peter</span> <span class="contact__last">Vosk</span></p>
      <p class="contact__title">Portfolio Manager</p>
      <p class="contact__phone">
        <svg viewBox="0 0 9 13" aria-hidden="true">
          <rect x="0.75" y="0.75" width="7.5" height="11.5" rx="1.2" fill="none" stroke="#1f1a78" stroke-width="1.5"/>
          <rect x="3" y="10" width="3" height="1" fill="#1f1a78"/>
        </svg>
        (482) 555-0137
      </p>
      <p class="contact__company">Morvane Holdings LLC</p>
      <p>2750 Birchwell Lane</p>
      <p>Suite 300, Atlanta GA 30327</p>
    </div>
  </section>

  <section class="card card--back">
    <div class="brand">
      <div class="brand__mark"></div>
      <div class="brand__name">Morvane Holdings</div>
      <div class="brand__rule"></div>
    </div>
  </section>
</body>
</html>
```